A register your interest postcard

It is a slightly bigger postcard that wil be inserted inside a brochure. On one side it is to have the logo with the statement "at Corvanne, Byron Bay" underneath. At the bottom it is to say "Register your interest to become an owner at The Keyholders Circle. On the flipside it has the logo in a smaller version with again in smaller writing "Become an owner at The Keyholders Circle". The main point of this side it to say " SMS your name to 0491 562 037 OR Name: Email: Phone:".
I would like a wood-look style postcard. It is for a luxury beach property that uses a lot of distressed wood in the building of the houses.
Industry/Entity Type
Building
Contact Information for Business Card
I would like a wood-look style postcard for a beach property.
Look and feel
Each slider illustrates characteristics of the customer's brand and the style your logo design should communicate.

```html
<!DOCTYPE html>
<html lang="en">
<head>
<meta charset="utf-8">
<title>The Keyholders Circle – Register your interest</title>
<link rel="stylesheet" href="https://fonts.googleapis.com/css2?family=Open+Sans:wght@400;700&display=swap">
<style>
  :root {
    --wood-dark: #2e150d;
    --wood-mid: #4a2317;
    --wood-warm: #5a2b1b;
    --ink-white: #ffffff;
    --accent-orange: #ee7a2c;
  }
  * { margin: 0; padding: 0; box-sizing: border-box; }
  html, body {
    width: 933px;
    height: 1200px;
    overflow: hidden;
    background: var(--wood-dark);
  }
  .postcard {
    position: relative;
    width: 933px;
    height: 1200px;
    overflow: hidden;
    font-family: "Open Sans", Arial, sans-serif;
  }
  .wood-surface {
    position: absolute;
    inset: 0;
    background:
      linear-gradient(90deg,
        var(--wood-dark) 0%,
        var(--wood-mid) 14%,
        var(--wood-dark) 27%,
        var(--wood-warm) 40%,
        var(--wood-mid) 55%,
        var(--wood-dark) 68%,
        var(--wood-warm) 82%,
        var(--wood-mid) 100%);
  }
  .brand-name {
    position: absolute;
    left: 97px;
    top: 76px;
    color: var(--ink-white);
    font-weight: 700;
    font-size: 92px;
    line-height: 128px;
    letter-spacing: -0.01em;
    text-transform: uppercase;
  }
  .brand-name span { display: block; }
  .location-line {
    position: absolute;
    left: 99px;
    top: 468px;
    color: var(--accent-orange);
    font-weight: 400;
    font-size: 35px;
    letter-spacing: 0.17em;
    text-transform: uppercase;
    white-space: nowrap;
  }
  .register-note {
    position: absolute;
    left: 96px;
    top: 970px;
    width: 282px;
    color: var(--accent-orange);
    font-weight: 400;
    font-size: 22px;
    line-height: 28px;
    text-align: justify;
  }
  .forward-arrows {
    position: absolute;
    left: 527px;
    top: 980px;
  }
</style>
</head>
<body>
  <main class="postcard">
    <div class="wood-surface" role="img" aria-label="Dark distressed wood grain background"></div>

    <h1 class="brand-name">
      <span>The</span>
      <span>Keyholders</span>
      <span>Circle</span>
    </h1>

    <p class="location-line">At Corvanne, Byron Bay</p>

    <p class="register-note">Register your interest to become an owner at The Keyholders Circle.</p>

    <svg class="forward-arrows" width="266" height="78" viewBox="0 0 266 78" aria-hidden="true">
      <polygon points="0,0 53,39 0,78" fill="#ffffff"/>
      <polygon points="105,0 158,39 105,78" fill="#ffffff"/>
      <polygon points="211,0 264,39 211,78" fill="#ffffff"/>
    </svg>
  </main>
</body>
</html>
```